Professional Business Card for Commercial Cleaning Company

We need a business card that represents our commercial janitorial cleaning company and represent several brands for our company so we do not want to highlight the logo too much. We want something that says we are professional.
Notes:No website or address as we have many locations and many websites and companies under our corporate name of "Brightvale Holdings, LLC" . Every time we hand a customer a business card they have contacted us via another brand we own but we don't want to have 21 business cards so we want to not focus on Brightvale Holdings, LLC too much since people will automatically ask "What is Brightvale Holdings, LLC" Example: Noodle Barn and Wrap Lantern restaurants are owned by "Zest! Brands" is the corporation name. Same principle here. Except we do not advertise at this time that all of our brands are connected. Hope this helps.
Target Market(s)
Commercial Cleaning
Industry/Entity Type
Janitorial Service
Contact Information for Business Card
Milo Jarvis
Business Development
555-382-9047
sales@brightvaleholdingsllc.example
Requirements
Must have
- Logo with contact information, need to be able to easily edit contact info for others in my office.
Nice to have
- Professional Image. Like to see a colorful bold look and a more standard business card look.
Should not have
- Any type of cleaning icons, tools, people or water.

```html
<!DOCTYPE html>
<html lang="en">
<head>
<meta charset="utf-8">
<title>Brightvale Holdings, LLC — Business Card</title>
<link href="https://fonts.googleapis.com/css2?family=Lato:wght@400;700&display=swap" rel="stylesheet">
<style>
  :root {
    --navy: #213f78;
    --green: #6aa843;
    --ink: #1c1c1c;
    --paper: #ffffff;
    --backdrop: #2b2b2b;
  }
  * { margin: 0; padding: 0; box-sizing: border-box; }
  html, body {
    width: 1189px;
    height: 1200px;
    overflow: hidden;
    background: var(--backdrop);
    font-family: "Lato", Arial, sans-serif;
  }
  .card {
    position: absolute;
    left: 171px;
    width: 856px;
    height: 489px;
    border-radius: 22px;
    overflow: hidden;
  }
  .card--front { top: 66px; background: var(--paper); }
  .card--back { top: 625px; background: var(--navy); }

  .brand-name {
    position: absolute;
    font-weight: 700;
    white-space: nowrap;
    letter-spacing: -0.3px;
  }
  .card--front .brand-name {
    left: 50px;
    top: 232px;
    font-size: 29px;
    color: var(--navy);
  }
  .card--back .brand-name {
    left: 0;
    right: 0;
    top: 235px;
    text-align: center;
    font-size: 50px;
    color: var(--paper);
  }

  .divider {
    position: absolute;
    left: 467px;
    top: 202px;
    width: 2px;
    height: 87px;
    background: var(--navy);
  }

  .contact {
    position: absolute;
    left: 500px;
    top: 175px;
  }
  .contact__name {
    font-size: 25px;
    font-weight: 700;
    color: var(--navy);
    line-height: 1.05;
  }
  .contact__role {
    font-size: 20px;
    color: var(--green);
    line-height: 1.15;
  }
  .contact__list {
    list-style: none;
    margin-top: 22px;
  }
  .contact__item {
    display: flex;
    align-items: center;
    gap: 10px;
    font-size: 19px;
    color: var(--ink);
    line-height: 28px;
    white-space: nowrap;
  }
  .contact__icon { width: 20px; height: 18px; flex: none; }
</style>
</head>
<body>
  <section class="card card--front" aria-label="Business card front">
    <div class="brand-name">Brightvale Holdings, LLC</div>
    <div class="divider"></div>
    <div class="contact">
      <p class="contact__name">Milo Jarvis</p>
      <p class="contact__role">Business Development</p>
      <ul class="contact__list">
        <li class="contact__item">
          <svg class="contact__icon" viewBox="0 0 20 18" aria-hidden="true">
            <rect x="5" y="1" width="10" height="16" rx="1.5" fill="none" stroke="#6aa843" stroke-width="2"/>
            <rect x="8.5" y="13.5" width="3" height="1.5" fill="#6aa843"/>
          </svg>
          <span>555-382-9047</span>
        </li>
        <li class="contact__item">
          <svg class="contact__icon" viewBox="0 0 20 18" aria-hidden="true">
            <rect x="0" y="3" width="20" height="13" fill="#6aa843"/>
            <path d="M0 3 L10 10.5 L20 3" fill="none" stroke="#ffffff" stroke-width="1.5"/>
            <path d="M0 16 L7.5 9 M20 16 L12.5 9" stroke="#ffffff" stroke-width="1.2"/>
          </svg>
          <span>sales@brightvaleholdingsllc.example</span>
        </li>
      </ul>
    </div>
  </section>

  <section class="card card--back" aria-label="Business card back">
    <div class="brand-name">Brightvale Holdings, LLC</div>
  </section>
</body>
</html>
```